Dinewell - iPad App Design Project

I have a iPad app that serves as a restaurant reservation system. The design that i currently have is very basic apple design. I am looking for it to have a much more professional appeal.

Please review the attached document which contains all of the screen shots for the app.
Updates

This Project has now been Guaranteed.  I look forward to reviewing your designs.

Brent

Reason: I am extending my deadline because i just changed this contest to guaranteed and have received a ton more "acceptances" because of it and I want to give those designers a chance to submit a design.

Target Market(s)

restaurant owners

Industry/Entity Type

Restaurant

Requirements
Must have
• On the seating chart i am changing the feature that shows the tables highlighted and instead would like that replace with a badge. So the list of wait staff across the top of the seating chart would instead have a number next to their name and would correspond with the badge on the table to determine their section.

So for example:
Ada would have a number 1 in front of her name and tables 18, 19, 20, and 31 would have a little badge in the upper right hand corner with the number "1" inside the badge.
Uma would have a number 2 in front of her name and tables 6, 7, and 11 would have a little badge in the upper right hand corner with the number " 2" inside the badge.
Nora would have a number 3 in front of her name and tables 12, 13, 27, 28, 29, and 30 would have a little badge in the upper right hand corner with the number " 3" inside the badge.

The names on the top will all be ONE color

Also, i would like an icon developed to replace the "C" you see next to some of the people's name in the reservation and waitlist slots. Also, i would like a better looking "check mark".

```html
<!DOCTYPE html>
<html lang="en">
<head>
<meta charset="utf-8">
<title>Dinewell – Host Stand</title>
<link rel="stylesheet" href="https://fonts.googleapis.com/css2?family=Open+Sans:wght@400;600;700;800&display=swap">
<style>
  :root {
    --screen-top: #3a3e46;
    --screen-bottom: #24272d;
    --bar-light: #f4f4f4;
    --bar-mid: #cfcfcf;
    --bar-dark: #a9a9a9;
    --brand: #2e8fc9;
    --text-light: #ffffff;
    --text-soft: #c9ccd2;
    --text-muted: #7d828b;
    --pill: #2a2d33;
    --pill-edge: #4a4e56;
    --row: #2c2f35;
    --eta: #b9d21a;
    --remove: #d8323a;
    --add: #3db24a;
    --card: #e6e6e6;
    --card-head-top: #e2e2e2;
    --card-head-bottom: #c6c6c6;
    --card-text: #8a8a8a;
    --card-head-text: #3b3b3b;
    --count: #5dbb52;
    --highlight: #f0a030;
    --dash: #bdbdbd;
  }
  * { box-sizing: border-box; margin: 0; padding: 0; }
  html, body { width: 1200px; height: 821px; overflow: hidden; }
  body {
    font-family: "Open Sans", sans-serif;
    background: linear-gradient(180deg, var(--screen-top), var(--screen-bottom));
    position: relative;
  }
  .app-frame {
    position: absolute; left: 8px; top: 18px; width: 1184px; height: 803px;
    border-radius: 26px 26px 0 0;
    background: linear-gradient(180deg, #3d414a 0%, #2b2e35 40%, #25282e 100%);
    box-shadow: inset 0 1px 0 rgba(255,255,255,.15);
  }
  .title-bar {
    position: absolute; left: 28px; top: 33px; width: 1153px; height: 72px;
    border-radius: 14px;
    background: linear-gradient(180deg, var(--bar-light) 0%, var(--bar-mid) 55%, var(--bar-dark) 100%);
    box-shadow: 0 2px 3px rgba(0,0,0,.5);
  }
  .brand-name {
    position: absolute; left: 0; right: 0; top: 14px; text-align: center;
    font-size: 38px; font-weight: 400; color: var(--brand); letter-spacing: -0.5px;
  }
  .bar-button {
    position: absolute; top: 18px; width: 52px; height: 38px; border-radius: 6px;
    background: linear-gradient(180deg, #8a8a8a, #5b5b5b);
    border: 1px solid #4a4a4a;
    display: flex; align-items: center; justify-content: center;
  }
  .bar-button.book { left: 1012px; }
  .bar-button.edit { left: 1072px; }

  .status-row { position: absolute; left: 0; top: 112px; width: 1200px; height: 60px; }
  .clock { position: absolute; left: 32px; top: 4px; font-size: 42px; font-weight: 700; color: var(--text-light); letter-spacing: -1px; }
  .meridiem { position: absolute; left: 162px; top: 10px; font-size: 15px; font-weight: 700; line-height: 19px; color: var(--text-light); }
  .meridiem .off { color: var(--text-muted); }
  .date { position: absolute; left: 188px; top: 8px; padding-left: 14px; border-left: 2px solid #5a5e66; font-size: 18px; font-weight: 800; line-height: 21px; color: var(--text-light); text-align: center; }
  .wait-pill {
    position: absolute; top: 6px; width: 166px; height: 46px; border-radius: 4px;
    background: var(--pill); border: 1px solid var(--pill-edge);
    text-align: center; color: var(--text-light);
  }
  .wait-pill .label { display: block; font-size: 17px; font-weight: 700; margin-top: 3px; }
  .wait-pill .value { display: block; font-size: 11px; color: var(--text-muted); margin-top: -2px; }
  .status-rule { position: absolute; left: 400px; right: 30px; top: 173px; border-top: 1px solid #555a62; }

  .wait-list { position: absolute; left: 13px; top: 207px; width: 320px; }
  .wait-list-head { display: flex; align-items: center; gap: 10px; height: 44px; padding-left: 8px; border-bottom: 2px dashed #b8bcc2; }
  .wait-list-head h2 { font-size: 21px; font-weight: 700; color: var(--text-light); }
  .guest {
    position: absolute; left: 0; width: 320px; height: 83px;
    background: var(--row); border-bottom: 1px solid #1c1e22;
    padding: 8px 0 0 13px;
  }
  .guest-name { font-size: 20px; color: var(--text-soft); line-height: 24px; }
  .guest-party { font-size: 13px; color: var(--text-muted); line-height: 16px; }
  .guest-eta { font-size: 20px; color: var(--eta); line-height: 24px; }
  .guest .remove { position: absolute; right: 14px; top: 27px; }

  .seating-panel {
    position: absolute; left: 354px; top: 205px; width: 810px; height: 616px;
    border-radius: 18px 18px 0 0;
    background: radial-gradient(ellipse at 55% 75%, #f2f2f2 0%, #bdbdbd 55%, #8e8e8e 100%);
  }
  .slot-card {
    position: absolute; width: 375px; height: 176px; border-radius: 8px;
    background: var(--card); overflow: hidden;
    box-shadow: 0 1px 3px rgba(0,0,0,.35);
  }
  .slot-head {
    position: relative; height: 43px;
    background: linear-gradient(180deg, var(--card-head-top), var(--card-head-bottom));
    border-bottom: 1px solid #b0b0b0;
  }
  .slot-time { position: absolute; left: 12px; top: 7px; font-size: 22px; font-weight: 700; color: var(--card-head-text); }
  .slot-fill { position: absolute; left: 148px; top: 14px; font-size: 12px; color: var(--card-text); }
  .slot-size { position: absolute; left: 222px; top: 12px; font-size: 15px; color: var(--card-text); }
  .slot-add { position: absolute; right: 8px; top: 7px; }
  .slot-rows { position: relative; padding-top: 10px; }
  .slot-rows::after { content: ""; position: absolute; left: 272px; top: 8px; bottom: -10px; border-left: 2px dashed var(--dash); }
  .slot-row { display: flex; height: 37px; align-items: center; font-size: 19px; color: var(--card-text); padding-left: 12px; }
  .slot-row .party { margin-left: auto; width: 128px; color: var(--count); }
  .slot-row.is-selected .guest-label { color: var(--highlight); }
</style>
</head>
<body>
  <div class="app-frame"></div>

  <header class="title-bar">
    <div class="brand-name">Dinewell</div>
    <div class="bar-button book" aria-label="Reservation book">
      <svg width="30" height="22" viewBox="0 0 30 22"><path d="M2 3h10q3 0 3 3v14q0-2-3-2H2zM28 3H18q-3 0-3 3v14q0-2 3-2h10z" fill="none" stroke="#fff" stroke-width="2"/></svg>
    </div>
    <div class="bar-button edit" aria-label="Edit">
      <svg width="26" height="24" viewBox="0 0 26 24"><path d="M17 3H3v18h18V9" fill="none" stroke="#fff" stroke-width="2"/><path d="M10 14l1-4 11-9 3 3-11 9z" fill="#fff"/></svg>
    </div>
  </header>

  <section class="status-row">
    <div class="clock">09:00</div>
    <div class="meridiem">AM<br><span class="off">PM</span></div>
    <div class="date">26 MAY<br>2012</div>
    <div class="wait-pill" style="left:400px"><span class="label">Avg Wait Time</span><span class="value">25 mins</span></div>
    <div class="wait-pill" style="left:571px"><span class="label">Avg Wait Time</span><span class="value">25 mins</span></div>
    <div class="wait-pill" style="left:770px"><span class="label">Avg Wait Time</span><span class="value">25 mins</span></div>
    <div class="wait-pill" style="left:962px"><span class="label">Avg Wait Time</span><span class="value">25 mins</span></div>
  </section>
  <div class="status-rule"></div>

  <aside class="wait-list">
    <div class="wait-list-head">
      <svg width="30" height="30" viewBox="0 0 30 30"><circle cx="15" cy="15" r="14" fill="#fff"/><circle cx="15" cy="15" r="11" fill="var(--add)"/><path d="M15 8v14M8 15h14" stroke="#fff" stroke-width="3.5"/></svg>
      <h2>Wait List</h2>
    </div>
    <div class="guest" style="top:39px"><div class="guest-name">Clara Hollis</div><div class="guest-party">Party of 4</div><div class="guest-eta">5m (2:02 PM)</div><svg class="remove" width="30" height="30" viewBox="0 0 30 30"><circle cx="15" cy="15" r="14" fill="#fff"/><circle cx="15" cy="15" r="11" fill="var(--remove)"/><path d="M8 15h14" stroke="#fff" stroke-width="3.5"/></svg></div>
    <div class="guest" style="top:136px"><div class="guest-name">Clara Hollis</div><div class="guest-party">Party of 4</div><div class="guest-eta">5m (2:02 PM)</div><svg class="remove" width="30" height="30" viewBox="0 0 30 30"><circle cx="15" cy="15" r="14" fill="#fff"/><circle cx="15" cy="15" r="11" fill="var(--remove)"/><path d="M8 15h14" stroke="#fff" stroke-width="3.5"/></svg></div>
    <div class="guest" style="top:233px"><div class="guest-name">Clara Hollis</div><div class="guest-party">Party of 4</div><div class="guest-eta">5m (2:02 PM)</div><svg class="remove" width="30" height="30" viewBox="0 0 30 30"><circle cx="15" cy="15" r="14" fill="#fff"/><circle cx="15" cy="15" r="11" fill="var(--remove)"/><path d="M8 15h14" stroke="#fff" stroke-width="3.5"/></svg></div>
    <div class="guest" style="top:330px"><div class="guest-name">Clara Hollis</div><div class="guest-party">Party of 4</div><div class="guest-eta">5m (2:02 PM)</div><svg class="remove" width="30" height="30" viewBox="0 0 30 30"><circle cx="15" cy="15" r="14" fill="#fff"/><circle cx="15" cy="15" r="11" fill="var(--remove)"/><path d="M8 15h14" stroke="#fff" stroke-width="3.5"/></svg></div>
    <div class="guest" style="top:427px"><div class="guest-name">Clara Hollis</div><div class="guest-party">Party of 4</div><div class="guest-eta">5m (2:02 PM)</div><svg class="remove" width="30" height="30" viewBox="0 0 30 30"><circle cx="15" cy="15" r="14" fill="#fff"/><circle cx="15" cy="15" r="11" fill="var(--remove)"/><path d="M8 15h14" stroke="#fff" stroke-width="3.5"/></svg></div>
  </aside>

  <main class="seating-panel">
    <article class="slot-card" style="left:20px;top:12px">
      <div class="slot-head"><span class="slot-time">12:15</span><span class="slot-fill">7/20</span><span class="slot-size">Size</span><svg class="slot-add" width="28" height="28" viewBox="0 0 28 28"><path d="M14 4v20M4 14h20" stroke="#fff" stroke-width="4"/></svg></div>
      <div class="slot-rows">
        <div class="slot-row"><span class="guest-label">Lorem Ipsum</span><span class="party">3</span></div>
        <div class="slot-row"><span class="guest-label">Lorem Ipsum</span><span class="party">4</span></div>
        <div class="slot-row"><span class="guest-label">Lorem Ipsum</span><span class="party">3</span></div>
      </div>
    </article>
    <article class="slot-card" style="left:415px;top:12px">
      <div class="slot-head"><span class="slot-time">12:15</span><span class="slot-fill">7/20</span><span class="slot-size">Size</span><svg class="slot-add" width="28" height="28" viewBox="0 0 28 28"><path d="M14 4v20M4 14h20" stroke="#fff" stroke-width="4"/></svg></div>
      <div class="slot-rows">
        <div class="slot-row"><span class="guest-label">Lorem Ipsum</span><span class="party">3</span></div>
        <div class="slot-row"><span class="guest-label">Lorem Ipsum</span><span class="party">4</span></div>
        <div class="slot-row"><span class="guest-label">Lorem Ipsum</span><span class="party">3</span></div>
      </div>
    </article>
    <article class="slot-card" style="left:20px;top:205px">
      <div class="slot-head"><span class="slot-time">12:15</span><span class="slot-fill">7/20</span><span class="slot-size">Size</span><svg class="slot-add" width="28" height="28" viewBox="0 0 28 28"><path d="M14 4v20M4 14h20" stroke="#fff" stroke-width="4"/></svg></div>
      <div class="slot-rows">
        <div class="slot-row"><span class="guest-label">Lorem Ipsum</span><span class="party">3</span></div>
        <div class="slot-row is-selected"><span class="guest-label">Lorem Ipsum</span><span class="party">4</span></div>
        <div class="slot-row"><span class="guest-label">Lorem Ipsum</span><span class="party">3</span></div>
      </div>
    </article>
    <article class="slot-card" style="left:415px;top:205px">
      <div class="slot-head"><span class="slot-time">12:15</span><span class="slot-fill">7/20</span><span class="slot-size">Size</span><svg class="slot-add" width="28" height="28" viewBox="0 0 28 28"><path d="M14 4v20M4 14h20" stroke="#fff" stroke-width="4"/></svg></div>
      <div class="slot-rows">
        <div class="slot-row"><span class="guest-label">Lorem Ipsum</span><span class="party">3</span></div>
        <div class="slot-row"><span class="guest-label">Lorem Ipsum</span><span class="party">4</span></div>
        <div class="slot-row"><span class="guest-label">Lorem Ipsum</span><span class="party">3</span></div>
      </div>
    </article>
    <article class="slot-card" style="left:20px;top:397px">
      <div class="slot-head"><span class="slot-time">12:15</span><span class="slot-fill">7/20</span><span class="slot-size">Size</span><svg class="slot-add" width="28" height="28" viewBox="0 0 28 28"><path d="M14 4v20M4 14h20" stroke="#fff" stroke-width="4"/></svg></div>
      <div class="slot-rows">
        <div class="slot-row"><span class="guest-label">Lorem Ipsum</span><span class="party">3</span></div>
        <div class="slot-row"><span class="guest-label">Lorem Ipsum</span><span class="party">4</span></div>
        <div class="slot-row"><span class="guest-label">Lorem Ipsum</span><span class="party">3</span></div>
      </div>
    </article>
  </main>
</body>
</html>
```